Q&W Night club Presents :

I need a advertiser 4 nights in one poster, from Thursday to Sunday,
Thursday : Every Thursday Irish Night
Friday: Old School Hip Hop, top 40 & request
Sat: Ripple Saturdays July 11, July 25, August 8, August 22
Brazilian Night Forro: July 18, August 1, August 15 & August 29
Sunday: Velvet Sundaze ( Dj Marlow & Dj Brevo

Target Market(s)

All 4 Nights

Industry/Entity Type

School

Font styles to use
Decorative
Script

Requirements
Must have
• Poster 11x16 and talk about all 4 nights on, see up there description
Nice to have
• A lot of colors
Should not have
• Address: 213 Calloway Rd Hyannis MA
• 5085550172
• Starting 9:30pm until 1:00Am
• 21+ ID
• Special Drinks $3.99

```html
<!DOCTYPE html>
<html lang="en">
<head>
<meta charset="utf-8">
<title>Q&amp;W Night Club – Four Nights Poster</title>
<link rel="stylesheet" href="https://fonts.googleapis.com/css2?family=Oswald:wght@400;500;700&family=Saira+Condensed:wght@500&display=swap">
<style>
  :root {
    --stage: #2d2d2d;
    --poster-black: #07060a;
    --steel-light: #f2f4f8;
    --steel-mid: #9aa3b3;
    --steel-dark: #4a5160;
    --night-yellow: #f3e21a;
    --request-red: #e3161c;
    --logo-gold: #f0c53a;
    --bar-light: #c9c9cc;
    --bar-dark: #3a3a3e;
  }
  * { margin: 0; padding: 0; box-sizing: border-box; }
  html, body {
    width: 872px; height: 1200px; overflow: hidden;
    background: var(--stage);
  }
  .poster {
    position: absolute; left: 36px; top: 18px;
    width: 800px; height: 1163px;
    background: var(--poster-black);
    overflow: hidden;
    box-shadow: 0 10px 30px rgba(0,0,0,.5);
  }
  .hero-photo {
    position: absolute; left: 0; top: 0; width: 800px; height: 456px;
    background:
      radial-gradient(circle at 88% 10%, rgba(255,110,20,.85) 0 9%, transparent 16%),
      radial-gradient(ellipse at 50% 78%, #e2461a 0 22%, #9a1c1a 38%, transparent 60%),
      radial-gradient(circle at 60% 10%, rgba(200,40,40,.5) 0 12%, transparent 24%),
      linear-gradient(180deg, #1a1418 0%, #0c0a10 100%);
  }
  .divider {
    position: absolute; left: 0; width: 800px; height: 14px;
    background: linear-gradient(180deg, var(--bar-light) 0%, #6d6d72 45%, var(--bar-dark) 100%);
  }
  .divider--upper { top: 456px; }
  .divider--lower { top: 908px; }
  .schedule {
    position: absolute; left: 0; top: 470px; width: 800px; height: 438px;
    background:
      radial-gradient(ellipse at 30% 90%, rgba(110,30,120,.55) 0 20%, transparent 45%),
      radial-gradient(ellipse at 75% 70%, rgba(80,20,70,.5) 0 18%, transparent 40%),
      radial-gradient(circle at 10% 40%, rgba(70,50,30,.4) 0 12%, transparent 28%),
      linear-gradient(180deg, #0d0b12 0%, #17101c 100%);
    text-align: center;
  }
  .night { position: absolute; left: 0; width: 100%; }
  .night-day {
    font-family: 'Oswald', sans-serif; font-weight: 700;
    font-size: 36px; line-height: 1; letter-spacing: .5px;
    text-transform: uppercase;
    background: linear-gradient(180deg, var(--steel-light) 0%, var(--steel-mid) 50%, var(--steel-dark) 52%, var(--steel-mid) 100%);
    -webkit-background-clip: text; background-clip: text; color: transparent;
    filter: drop-shadow(0 2px 2px rgba(0,0,0,.9));
  }
  .night-detail {
    font-family: 'Oswald', sans-serif; font-weight: 400;
    font-size: 22px; line-height: 1; text-transform: uppercase;
    color: var(--night-yellow);
    text-shadow: 0 2px 2px rgba(0,0,0,.9);
  }
  .night-detail .aside {
    font-family: 'Saira Condensed', sans-serif; text-transform: none;
    color: var(--request-red); margin-left: 6px;
  }
  .lights {
    position: absolute; left: 0; top: 922px; width: 800px; height: 241px;
    background:
      radial-gradient(circle at 12% 55%, #d2338f 0 16%, transparent 30%),
      radial-gradient(circle at 88% 60%, #d8305c 0 18%, transparent 32%),
      radial-gradient(circle at 42% 20%, rgba(220,60,60,.8) 0 10%, transparent 20%),
      radial-gradient(circle at 70% 30%, rgba(120,40,170,.8) 0 12%, transparent 26%),
      linear-gradient(90deg, #8c1f8a 0%, #3a1550 50%, #7a1c46 100%);
  }
  .club-name {
    position: absolute; left: 146px; top: 994px; width: 481px; height: 93px;
    display: flex; align-items: center; justify-content: center;
    background: rgba(14,8,20,.85);
    font-family: 'Oswald', sans-serif; font-weight: 500;
    font-size: 56px; letter-spacing: 1px; text-transform: uppercase;
    color: var(--logo-gold);
  }
</style>
</head>
<body>
  <main class="poster">
    <div class="hero-photo" role="img" aria-label="Club photo collage with a dancer, party lights, sparkles and disco ball"></div>
    <div class="divider divider--upper"></div>

    <section class="schedule" role="img" aria-label="Dark collage of champagne bottles and party lights behind the weekly schedule">
      <div class="night" style="top:20px"><h2 class="night-day">Thursday</h2></div>
      <div class="night" style="top:64px"><p class="night-detail">Every Thursday Irish Night</p></div>
      <div class="night" style="top:99px"><h2 class="night-day">Friday</h2></div>
      <div class="night" style="top:146px"><p class="night-detail">Old School Hip Hop<span class="aside">[top 40 &amp; request]</span></p></div>
      <div class="night" style="top:185px"><h2 class="night-day">Saturday</h2></div>
      <div class="night" style="top:231px"><p class="night-detail">Ripple Saturdays July 11, July 25, August 8, August 22</p></div>
      <div class="night" style="top:271px"><h2 class="night-day">Brazilian Night Forro</h2></div>
      <div class="night" style="top:313px"><p class="night-detail">July 18, August 1, August 15 &amp; August 29</p></div>
      <div class="night" style="top:350px"><h2 class="night-day">Sunday</h2></div>
      <div class="night" style="top:396px"><p class="night-detail">Velvet Sundaze ( Dj Marlow &amp; Dj Brevo</p></div>
    </section>

    <div class="divider divider--lower"></div>
    <div class="lights" role="img" aria-label="Colourful bokeh light circles in pink, purple and red"></div>
    <h1 class="club-name">Q&amp;W Night Club</h1>
  </main>
</body>
</html>
```